Veltrix Global Policy Document/Report Template for consistent document outputs

We need a policy document/report template that we can disseminate to staff so all produced documents look the same, and less formatting has to be done each time a policy or report is started.
VGL applies the power of biological science, physical science, and IT to solve the most challenging mission problems encompassing Forensics, Biometrics, Weapons Technical and Identity Intelligence, CBRNE, CWMD, and Public Health initiatives. Here is a list of requirements for the document:
• Cover page
o Include full logo
o Title
o Possibly a subtitle
o Version #
o Date
o We want a common look that all policy documents will follow, and it is easy to recognize
o Some color and a unique look and feel
• Header and Footer (2nd page on)
o Both header and footer must include this language: “Confidential and Proprietary - For Veltrix Global Internal Use Only,” so it appears at the top and bottom of the page
o The document title must be in either the header or footer
• Header (after first page)
o Include logo
• Footer (not counting title page)
o Must include date, and page X of Y
• 4 levels of headings, numbered 1, 1.1, 1.1.1, 1.1.1.1
• 4 levels of bullets with color/style
• Design for a callout box
• Design or a box containing a quote
• Two table designs
• Pages (other than the title page)
o Pages are primarily white
o Colors for accent and visual interest

Finally, our corporate font is Source Sans Pro.
The swirl pattern on our logo has no special meaning (but feel free to use it as a design element).

Font styles to use
Other font styles liked:
• Source Sans Pro

Requirements
Must have
• See description for more information: Cover page, header and footer, multiple heading levels, callout box, tables

```html
<!DOCTYPE html>
<html lang="en">
<head>
<meta charset="utf-8">
<title>Veltrix Global Report Template</title>
<link rel="stylesheet" href="https://fonts.googleapis.com/css2?family=Quicksand:wght@400;500;600;700&display=swap">
<style>
:root{
  --backdrop:#7a7879;
  --paper:#ffffff;
  --navy:#2b2f8e;
  --purple:#5a2a7f;
  --plum:#862060;
  --crimson:#d0283e;
  --ink:#3f3f46;
  --muted:#6b6b73;
  --quote:#808084;
  --rule:#d9d9dc;
  --band:linear-gradient(90deg,#2d2f8f 0%,#58287d 55%,#8a1f5b 100%);
}
*{margin:0;padding:0;box-sizing:border-box}
html,body{width:1200px;height:606px;overflow:hidden}
body{background:var(--backdrop);font-family:"Quicksand",sans-serif;position:relative;color:var(--ink)}
.page{position:absolute;background:var(--paper);width:173.3px;height:219.6px;overflow:hidden}
.abs{position:absolute}
.template-label{position:absolute;left:174.6px;top:264px;font-size:4.6px;color:#222;letter-spacing:.1px}

/* company name in place of brand mark */
.brand-name{position:absolute;font-weight:600;color:var(--navy);line-height:1;white-space:nowrap}
.head-brand{right:10px;top:11px;font-size:7px}
.cover-brand,.toc-brand{left:0;right:0;text-align:center;font-size:15px}
.cover-brand{top:38px}
.toc-brand{top:40px}

/* header / footer */
.conf{position:absolute;left:12px;top:9.5px;font-size:2.3px;color:var(--muted)}
.doc-title{position:absolute;left:11.5px;top:15px;font-size:7.4px;font-weight:600;color:var(--navy);letter-spacing:.2px}
.foot-line{position:absolute;left:0;right:0;bottom:9.8px;height:.9px;background:var(--navy)}
.foot{position:absolute;left:0;right:0;bottom:0;height:8.6px;background:var(--band);color:#fff;font-size:2.3px;display:flex;align-items:center;padding-left:12px}
.foot .date{position:absolute;left:132px}
.foot .pg{position:absolute;left:155px}

.txt{font-size:3px;line-height:4px;color:var(--ink);text-align:justify}
.h-side{font-size:5.2px;color:var(--navy);font-weight:500;letter-spacing:.2px}

/* cover */
.cover{left:23.8px;top:31.2px;width:348.4px;height:219.9px;box-shadow:0 6px 14px rgba(0,0,0,.35)}
.cover-panel{position:absolute;left:0;top:0;width:174.2px;height:100%;background:linear-gradient(150deg,#3a3b9c 0%,#4f2d86 45%,#7a1f60 100%)}
.cover-contact{position:absolute;left:0;width:174.2px;text-align:center;color:#fff;font-size:3.3px;font-weight:500}
.cover-sheet{position:absolute;left:174.2px;top:0;width:174.2px;height:100%}
.cover-year{position:absolute;left:0;right:0;top:78px;text-align:center;font-size:20px;font-weight:700;color:var(--navy)}
.cover-title{position:absolute;left:0;right:0;top:101px;text-align:center;font-size:12.4px;font-weight:700;color:var(--crimson);letter-spacing:.2px}
.cover-sub{position:absolute;left:0;right:0;top:119px;text-align:center;font-size:6.8px;font-weight:600;color:var(--purple)}
.cover-meta{position:absolute;left:42px;top:133px;font-size:6.8px;font-weight:600;color:var(--purple);display:flex;gap:9px}
.cover-by{position:absolute;left:14px;top:156px;font-size:7.6px;font-weight:600;color:var(--muted)}
.cover-name{position:absolute;left:14px;top:174px;font-size:6.6px;font-weight:600;color:var(--muted);line-height:8px}

/* contents */
.toc-title{position:absolute;left:21px;top:82px;font-size:8.6px;font-weight:600;color:var(--navy);letter-spacing:.2px}
.toc-list{position:absolute;left:25px;top:101px;width:112px;list-style:none}
.toc-list li{display:flex;align-items:center;height:12.6px;border-bottom:.8px dotted var(--navy);font-size:6.2px;color:var(--muted)}
.toc-list li:last-child{border-bottom:none}
.toc-list .num{width:6.5px;height:6.5px;border-radius:50%;background:var(--navy);color:#fff;font-size:3.6px;font-weight:700;display:flex;align-items:center;justify-content:center;margin-right:5px}

/* services */
.svc-icon{position:absolute;left:23px;width:12px;height:12px;border-radius:50%;background:var(--navy);display:flex;align-items:center;justify-content:center}
.svc-icon span{width:6px;height:6px;border:1px solid #fff;border-radius:50%}
.svc-name{position:absolute;left:43px;font-size:5.2px;color:var(--navy);font-weight:500}
.svc-text{position:absolute;left:43px;width:104px;font-size:3.6px;line-height:4.7px;color:var(--muted)}

/* photo page */
.photo{position:absolute;left:10.7px;top:43px;width:56.5px;height:147px;background:#52277a;display:flex;align-items:center;justify-content:center}
.photo span{color:#fff;font-size:8.5px;writing-mode:vertical-rl;letter-spacing:.4px}
.feature-h{position:absolute;left:80px;font-size:7.2px;color:var(--navy);font-weight:500}
.feature-t{position:absolute;left:80px;width:78px;font-size:3.6px;line-height:4.8px;color:var(--muted)}

/* headings page */
.hd{position:absolute;color:var(--muted);font-weight:500}
.hd1{font-size:7px}
.hd2{font-size:5.8px}
.hd3{font-size:5.6px}
.hd4{font-size:5.6px}

/* bullets */
.blk-h{position:absolute;left:12.6px;font-size:6.2px;color:var(--muted);font-weight:500}
.bullets{position:absolute;left:31px;width:142px;list-style:none}
.bullets li{position:relative;padding-left:4.5px;font-size:3px;line-height:3.6px;color:var(--ink);margin-bottom:3.1px;padding-right:8px}
.bullets li::before{content:"";position:absolute;left:-4px;top:1px;width:1.6px;height:1.6px;background:var(--navy)}
.bullets.numbered{counter-reset:n}
.bullets.numbered li::before{counter-increment:n;content:counter(n);background:none;width:auto;height:auto;top:0;left:-4.5px;color:var(--muted);font-size:3px}

/* quote page */
.quote{position:absolute;left:13px;width:53px;background:var(--quote);color:#fff;font-style:italic;font-size:3.4px;line-height:4.8px;text-align:center;padding:6px 4px;display:flex;align-items:flex-start;justify-content:center}
.quote-text{position:absolute;left:80px;width:81px;font-size:3.4px;line-height:4.7px;color:var(--ink)}

/* callout page */
.call-h{position:absolute;left:15px;font-size:6.2px;color:var(--navy);font-weight:500}
.callout{position:absolute;left:29px;width:119px;height:32.5px;background:var(--quote);border:.8px solid #5e5e63;color:#fff;font-style:italic;font-size:3px;line-height:4.5px;padding:4px 7px}
.call-t{position:absolute;left:15px;width:146px;font-size:3.2px;line-height:4.5px;color:var(--ink)}

/* tables */
.report-table{position:absolute;left:13px;top:40.5px;width:145px;font-size:2.4px;color:#222}
.report-table .r{display:flex;height:6.05px;align-items:center}
.report-table .bar{background:#d6d6d8;padding-left:1px}
.report-table .red{color:var(--crimson)}
.report-table .c1{width:27px;padding-left:1px}
.report-table .c2{width:45px}
.report-table .c3{width:27px}
.report-table .ca{width:84px;padding-left:1px}
.report-table .cb{width:28px}
.report-table .gap{height:3px}

.sheet-label{position:absolute;left:13px;top:39px;font-size:2.4px;color:#222}
.grid{position:absolute;left:13px;width:146px;border-collapse:collapse;font-size:2.2px;color:#222}
.grid td{border:.5px solid #333;height:5.7px;padding:0 1px;white-space:nowrap}
.grid td.rt{text-align:right}
.info-grid td{height:5.4px}
.sign{position:absolute;left:13px;top:189px;width:146px;height:11px;border:.5px solid #333;font-size:2.3px;padding:1px 1.5px;line-height:3.2px}
</style>
</head>
<body>

<div class="template-label">REPORT TEMPLATE</div>

<!-- Cover spread -->
<section class="page cover">
  <div class="cover-panel">
    <p class="cover-contact" style="top:195px">VGL / 555-010-2040</p>
    <p class="cover-contact" style="top:202px;font-size:3.1px">P :+555-01-277 &nbsp;E : info@vgl-mail.com W : www.vgl-example.com</p>
  </div>
  <div class="cover-sheet">
    <p class="brand-name cover-brand">Veltrix Global</p>
    <h1 class="cover-year">2023</h1>
    <h2 class="cover-title">REPORT TITLE</h2>
    <p class="cover-sub">Project Update November 2023</p>
    <p class="cover-meta"><span>Version #</span><span>Date : 26/03/24</span></p>
    <p class="cover-by">Prepared By</p>
    <p class="cover-name">Name<br>Company name</p>
    <div class="foot-line"></div>
    <div class="foot"></div>
  </div>
</section>

<!-- Contents -->
<section class="page" style="left:398.3px;top:31.2px;height:219.9px">
  <p class="brand-name toc-brand">Veltrix Global</p>
  <h2 class="toc-title">Table of content</h2>
  <ol class="toc-list">
    <li><span class="num">1</span>Unde omnis iste natus</li>
    <li><span class="num">2</span>Accusantium doloremque</li>
    <li><span class="num">3</span>Laudantium, totam</li>
    <li><span class="num">4</span>Eaque ipsa</li>
  </ol>
  <div class="foot-line"></div>
  <div class="foot"></div>
</section>

<!-- Charts page -->
<section class="page" style="left:601.4px;top:31.2px;height:219.9px">
  <p class="conf">"Confidential and Proprietary - For Veltrix Global Internal Use Only,"</p>
  <h2 class="doc-title">DOCUMENT TITLE</h2>
  <p class="brand-name head-brand">Veltrix Global</p>

  <svg class="abs" style="left:11px;top:56px" width="82" height="54" viewBox="0 0 82 54" role="img" aria-label="Bar chart of weekday values">
    <g font-size="2.4" fill="#333" font-family="Quicksand, sans-serif">
      <text x="0" y="4">50</text><text x="0" y="13">40</text><text x="0" y="22">30</text><text x="0" y="31">20</text><text x="0" y="40">10</text><text x="2" y="49">0</text>
      <text x="6" y="53">Mon</text><text x="20" y="53">Tues</text><text x="35" y="53">Wed</text><text x="49" y="53">Thurs</text><text x="64" y="53">Friday</text>
    </g>
    <line x1="5" y1="48" x2="80" y2="48" stroke="#999" stroke-width=".3"/>
    <g fill="#2b2f8e">
      <rect x="7" y="3" width="7" height="45"/>
      <rect x="21" y="30" width="7" height="18"/>
      <rect x="36" y="12" width="7" height="36"/>
      <rect x="50" y="21" width="7" height="27"/>
      <rect x="66" y="3" width="7" height="45"/>
    </g>
  </svg>

  <p class="abs h-side" style="left:99px;top:58.5px">SIDE HEADING</p>
  <p class="abs txt" style="left:98.5px;top:65.5px;width:64px;font-size:4.3px;line-height:5.6px">"Lorem ipsum dolor sit amet, consectetur adipiscing elit, sed do eiusmod tempor incididunt ut labore et dolore magna aliqua. Ut enim ad minim veniam, quis nostrud exer-</p>

  <p class="abs h-side" style="left:17px;top:119px">SIDE HEADING</p>
  <p class="abs txt" style="left:17px;top:126px;width:75px;font-size:4.2px;line-height:5.1px">"Lorem ipsum dolor sit amet, consectetur adipiscing elit, sed do eiusmod tempor incididunt ut labore et irure dolor in reprehen-</p>
  <p class="abs h-side" style="left:17px;top:161px">SIDE HEADING</p>
  <p class="abs txt" style="left:17px;top:168.5px;width:75px;font-size:4.2px;line-height:5.1px">"Lorem ipsum dolor sit amet, consectetur adipiscing elit, sed do eiusmod tempor incididunt ut labore et irure dolor in reprehen-</p>

  <svg class="abs" style="left:97px;top:137px" width="66" height="52" viewBox="0 0 66 52" role="img" aria-label="Line chart of weekday values">
    <g font-size="2.2" fill="#333" font-family="Quicksand, sans-serif">
      <text x="0" y="4">50</text><text x="0" y="12">40</text><text x="0" y="20">30</text><text x="0" y="28">20</text><text x="0" y="36">10</text><text x="1" y="44">0</text>
      <text x="8" y="50">Mon</text><text x="20" y="50">Tues</text><text x="32" y="50">Wed</text><text x="44" y="50">Thurs</text><text x="58" y="50">Fri</text>
    </g>
    <g stroke="#e2e2e4" stroke-width=".3"><line x1="5" y1="3" x2="64" y2="3"/><line x1="5" y1="11" x2="64" y2="11"/><line x1="5" y1="19" x2="64" y2="19"/><line x1="5" y1="27" x2="64" y2="27"/><line x1="5" y1="35" x2="64" y2="35"/><line x1="5" y1="43" x2="64" y2="43"/></g>
    <polyline points="10,19 23,27 35,11 48,19 61,3" fill="none" stroke="#2b2f8e" stroke-width="1"/>
  </svg>

  <div class="foot-line"></div>
  <div class="foot"><span>"Confidential and Proprietary - For Veltrix Global Internal Use Only,"</span><span class="date">26/03/24</span><span class="pg">X of Y</span></div>
</section>

<!-- Services page -->
<section class="page" style="left:799.4px;top:31.2px;height:219.9px">
  <p class="conf">"Confidential and Proprietary - For Veltrix Global Internal Use Only,"</p>
  <h2 class="doc-title">DOCUMENT TITLE</h2>
  <p class="brand-name head-brand">Veltrix Global</p>

  <div class="svc-icon" style="top:42px"><span></span></div>
  <p class="svc-name" style="top:42.5px">Identify Management Services</p>
  <p class="svc-text" style="top:50px">"Lorem ipsum dolor sit amet, consectetur adipiscing elit, sed do eiusmod tempor incididunt ut labore et dolore magna aliqua. Ut enim ad minim veniam, quis nostrud exercitation ullamco</p>

  <div class="svc-icon" style="top:79px"><span></span></div>
  <p class="svc-name" style="top:81px">Access management Services</p>
  <p class="svc-text" style="top:88.5px">"Lorem ipsum dolor sit amet, consectetur adipiscing elit, sed do eiusmod tempor incididunt ut labore et dolore magna aliqua. Ut enim ad minim veniam, quis nostrud exercitation ullamco laboris</p>

  <div class="svc-icon" style="top:119px"><span></span></div>
  <p class="svc-name" style="top:120.5px">Credential Access Management</p>
  <p class="svc-text" style="top:128px">"Lorem ipsum dolor sit amet, consectetur adipiscing elit, sed do eiusmod tempor incididunt ut labore et dolore magna aliqua. Ut enim ad minim veniam, quis nostrud exercitation ullamco laboris nisi ut aliquip ex ea commodo consequat. Duis</p>

  <div class="svc-icon" style="top:158px"><span></span></div>
  <p class="svc-name" style="top:162.5px">Capital &nbsp;Management</p>
  <p class="svc-text" style="top:171px">"Lorem ipsum dolor sit amet, consectetur adipiscing elit, sed do eiusmod tempor incididunt ut labore et dolore magna aliqua. Ut enim ad minim veniam, quis nostrud exercitation ullamco laboris nisi ut aliquip ex ea commodo consequat. Duis</p>

  <div class="foot-line"></div>
  <div class="foot"></div>
</section>

<!-- Photo feature page -->
<section class="page" style="left:991.3px;top:31.2px;height:219.9px">
  <p class="conf">"Confidential and Proprietary - For Veltrix Global Internal Use Only,"</p>
  <h2 class="doc-title">DOCUMENT TITLE</h2>
  <p class="brand-name head-brand" style="top:14px">Veltrix Global</p>

  <div class="photo" role="img" aria-label="Photo placeholder"><span>Photo Here</span></div>

  <p class="feature-h" style="top:46px">side heading here</p>
  <p class="feature-t" style="top:56px">"Lorem ipsum dolor sit amet, consectetur adipiscing elit, sed do eiusmod tempor incididunt ut labore et dolore magna aliqua. Ut enim ad minim veniam, quis nostrud exercitation</p>
  <p class="feature-h" style="top:96px">side heading here</p>
  <p class="feature-t" style="top:106px">"Lorem ipsum dolor sit amet, consectetur adipiscing elit, sed do eiusmod tempor incididunt ut labore et dolore magna aliqua. Ut enim ad minim veniam, quis nostrud exercitation</p>
  <p class="feature-h" style="top:146px">side heading here</p>
  <p class="feature-t" style="top:156px">"Lorem ipsum dolor sit amet, consectetur adipiscing elit, sed do eiusmod tempor incididunt ut labore et dolore magna aliqua. Ut enim ad minim veniam, quis nostrud exercitation</p>

  <div class="foot-line"></div>
  <div class="foot"></div>
</section>

<!-- Heading levels page -->
<section class="page" style="left:16.8px;top:296.3px">
  <p class="conf">"Confidential and Proprietary - For Veltrix Global Internal Use Only,"</p>
  <h2 class="doc-title">DOCUMENT TITLE</h2>
  <p class="brand-name head-brand">Veltrix Global</p>

  <h3 class="hd hd1" style="left:13px;top:27.5px">1. Main heading</h3>
  <p class="abs txt" style="left:13px;top:38px;width:148px">"Lorem ipsum dolor sit amet, consectetur adipiscing elit, sed do eiusmod tempor incididunt ut labore et irure dolor in reprehenderit in voluptate velit esse cillum dolore eu fugiat nulla pariatur. Excepteur sint occaecat cupidatat non proident, sunt in culpa qui officia deserunt mollit anim id est laborum."</p>

  <h4 class="hd hd2" style="left:18px;top:58px">1.1 sub heading</h4>
  <p class="abs txt" style="left:31px;top:64.5px;width:130px">"Lorem ipsum dolor sit amet, consectetur adipiscing elit, sed do eiusmod tempor incididunt ut labore et irure dolor in reprehenderit in voluptate velit esse cillum dolore eu fugiat nulla pariatur. Excepteur sint occaecat cupidatat non proident, sunt in culpa qui officia deserunt mollit anim id est laborum."</p>

  <h5 class="hd hd3" style="left:25.6px;top:92px">1.1.1Sub heading</h5>
  <p class="abs txt" style="left:35px;top:101px;width:126px">"Lorem ipsum dolor sit amet, consectetur adipiscing elit, sed do eiusmod tempor incididunt ut labore et irure dolor in reprehenderit in voluptate velit esse cillum dolore eu fugiat nulla pariatur. Excepteur sint occaecat cupidatat non proident, sunt in culpa qui officia deserunt mollit anim id est laborum."Lorem ipsum dolor sit amet, consectetur adipiscing elit, sed do eiusmod tempor incididunt ut labore et irure dolor in reprehenderit in voluptate velit esse cillum dolore eu fugiat nulla pariatur. Excepteur sint occaecat cupidatat</p>

  <h6 class="hd hd4" style="left:38px;top:141px">1.1.1.1 Sub heading</h6>
  <p class="abs txt" style="left:46px;top:150px;width:115px">"Lorem ipsum dolor sit amet, consectetur adipiscing elit, sed do eiusmod tempor incididunt ut labore et irure dolor in reprehenderit in voluptate velit esse cillum dolore eu fugiat nulla pariatur. Excepteur sint occaecat cupidatat non proident, sunt in culpa qui officia deserunt mollit anim id est laborum."</p>
  <p class="abs txt" style="left:46px;top:181px;width:115px">"Lorem ipsum dolor sit amet, consectetur adipiscing elit, sed do eiusmod tempor incididunt ut labore et irure dolor in reprehenderit in voluptate velit esse cillum dolore eu fugiat nulla pariatur. Excepteur sint occaecat cupidatat non</p>

  <div class="foot-line"></div>
  <div class="foot"><span>"Confidential and Proprietary - For Veltrix Global Internal Use Only,"</span><span class="date">26/03/24</span><span class="pg">X of Y</span></div>
</section>

<!-- Bullet lists page -->
<section class="page" style="left:214.7px;top:296.3px">
  <p class="conf" style="top:12.5px">"Confidential and Proprietary - For Veltrix Global Internal Use Only,"</p>
  <h2 class="doc-title" style="top:18.5px">DOCUMENT TITLE</h2>
  <p class="brand-name head-brand" style="top:14px">Veltrix Global</p>

  <h3 class="blk-h" style="top:29.5px">Heading</h3>
  <ul class="bullets" style="top:38.5px">
    <li>"Lorem ipsum dolor sit amet, consectetur adipiscing elit, sed do eiusmod tempor incididunt ut lit in voluptate velit esse cillum dolore eu fugiat nulla</li>
    <li>"Lorem ipsum dolor sit amet, consectetur adipiscing elit, sed do eiusmod tempor incididunt ut lit in voluptate velit esse cillum dolore eu fugiat nulla</li>
    <li>"Lorem ipsum dolor sit amet, consectetur adipiscing elit, sed do eiusmod tempor incididunt ut lit in voluptate velit esse cillum dolore eu fugiat nulla</li>
    <li>"Lorem ipsum dolor sit amet, consectetur adipiscing elit, sed do eiusmod tempor incididunt ut lit in voluptate velit esse cillum dolore eu fugiat nulla</li>
    <li>"Lorem ipsum dolor sit amet, consectetur adipiscing elit, sed do eiusmod tempor incididunt ut lit in voluptate velit esse cillum dolore eu fugiat nulla</li>
  </ul>
  <h3 class="blk-h" style="top:89.5px">Heading</h3>
  <ul class="bullets" style="top:101.5px">
    <li>"Lorem ipsum dolor sit amet, consectetur adipiscing elit, sed do eiusmod tempor incididunt ut lit in voluptate velit esse cillum dolore eu fugiat nulla</li>
    <li>"Lorem ipsum dolor sit amet, consectetur adipiscing elit, sed do eiusmod tempor incididunt ut lit in voluptate velit esse cillum dolore eu fugiat nulla</li>
    <li>"Lorem ipsum dolor sit amet, consectetur adipiscing elit, sed do eiusmod tempor incididunt ut lit in voluptate velit esse cillum dolore eu fugiat nulla</li>
    <li>"Lorem ipsum dolor sit amet, consectetur adipiscing elit, sed do eiusmod tempor incididunt ut lit in voluptate velit esse cillum dolore eu fugiat nulla</li>
    <li>"Lorem ipsum dolor sit amet, consectetur adipiscing elit, sed do eiusmod tempor incididunt ut lit in voluptate velit esse cillum dolore eu fugiat nulla</li>
  </ul>
  <h3 class="blk-h" style="top:152.5px">Heading</h3>
  <ol class="bullets numbered" style="top:161.5px">
    <li>"Lorem ipsum dolor sit amet, consectetur adipiscing elit, sed do eiusmod tempor incididunt ut lit in voluptate velit esse cillum dolore eu fugiat nulla</li>
    <li>"Lorem ipsum dolor sit amet, consectetur adipiscing elit, sed do eiusmod tempor incididunt ut lit in voluptate velit esse cillum dolore eu fugiat nulla</li>
    <li>"Lorem ipsum dolor sit amet, consectetur adipiscing elit, sed do eiusmod tempor incididunt ut lit in voluptate velit esse cillum dolore eu fugiat nulla</li>
    <li>"Lorem ipsum dolor sit amet, consectetur adipiscing elit, sed do eiusmod tempor incididunt ut lit in voluptate velit esse cillum dolore eu fugiat nulla</li>
  </ol>

  <div class="foot-line"></div>
  <div class="foot"><span>"Confidential and Proprietary - For Veltrix Global Internal Use Only,"</span><span class="date">26/03/24</span><span class="pg">X of Y</span></div>
</section>

<!-- Quote page -->
<section class="page" style="left:409.9px;top:296.3px">
  <p class="conf" style="top:14.5px">"Confidential and Proprietary - For Veltrix Global Internal Use Only,"</p>
  <h2 class="doc-title" style="top:20.5px">DOCUMENT TITLE</h2>
  <p class="brand-name head-brand" style="top:16px">Veltrix Global</p>

  <blockquote class="quote" style="top:32px;height:49px">"Lorem ipsum dolor sit amet, consectetur adipiscing elit, sed do eiusmod tempor incididunt ut labore et dolore magna aliqua. Ut enim ad minim veniam, quis nostrud</blockquote>
  <p class="quote-text" style="top:35px">"Lorem ipsum dolor sit amet, consectetur adipiscing elit, sed do eiusmod tempor incididunt ut labore et dolore magna aliqua. Ut enim ad minim veniam, quis nostrud exercitation ullamco laboris nisi ut aliquip ex ea commodo consequat. Duis aute irure dolor in reprehenderit in voluptate velit esse cillum dolore eu fugiat nulla pariatur. Excepteur sint occaecat cupidatat non proident, sunt in culpa qui officia deserunt</p>

  <blockquote class="quote" style="top:89.5px;height:52px">"Lorem ipsum dolor sit amet, consectetur adipiscing elit, sed do eiusmod tempor incididunt ut labore et dolore magna aliqua. Ut enim ad minim veniam, quis nostrud</blockquote>
  <p class="quote-text" style="top:94px">"Lorem ipsum dolor sit amet, consectetur adipiscing elit, sed do eiusmod tempor incididunt ut labore et dolore magna aliqua. Ut enim ad minim veniam, quis nostrud exercitation ullamco laboris nisi ut aliquip ex ea commodo consequat. Duis aute irure dolor in reprehenderit in voluptate velit esse cillum dolore eu fugiat nulla pariatur. Excepteur sint occaecat cupidatat non proident, sunt in culpa qui officia deserunt</p>

  <blockquote class="quote" style="top:147.7px;height:52.5px">"Lorem ipsum dolor sit amet, consectetur adipiscing elit, sed do eiusmod tempor incididunt ut labore et dolore magna aliqua. Ut enim ad minim veniam, quis nostrud</blockquote>
  <p class="quote-text" style="top:152px">"Lorem ipsum dolor sit amet, consectetur adipiscing elit, sed do eiusmod tempor incididunt ut labore et dolore magna aliqua. Ut enim ad minim veniam, quis nostrud exercitation ullamco laboris nisi ut aliquip ex ea commodo consequat. Duis aute irure dolor in reprehenderit in voluptate velit esse cillum dolore eu fugiat nulla pariatur. Excepteur sint occaecat cupidatat non proident, sunt in culpa qui officia deserunt</p>

  <div class="foot-line"></div>
  <div class="foot"><span>"Confidential and Proprietary - For Veltrix Global Internal Use Only,"</span><span class="date">26/03/24</span><span class="pg">X of Y</span></div>
</section>

<!-- Callout page -->
<section class="page" style="left:607.4px;top:296.3px">
  <p class="conf" style="top:12.5px;left:14px">"Confidential and Proprietary - For Veltrix Global Internal Use Only,"</p>
  <h2 class="doc-title" style="top:18.5px;left:13px">DOCUMENT TITLE</h2>
  <p class="brand-name head-brand" style="top:14px">Veltrix Global</p>

  <h3 class="call-h" style="top:28.5px">Lorem ipsum dolor sit amet, cons :</h3>
  <p class="call-t" style="top:39px">"Lorem ipsum dolor sit amet, consectetur adipiscing elit, sed do eiusmod tempor incididunt ut labore et dolore magna aliqua. Ut enim ad minim veniam, quis nostrud exercitation ullamco laboris nisi ut aliquip ex ea commodo consequat. Duis aute irure dolor in</p>
  <aside class="callout" style="top:61.5px">"Lorem ipsum dolor sit amet, consectetur adipiscing elit, sed do eiusmod tempor incididunt ut labore et dolore magna aliqua. Ut enim ad minim veniam, quis nostrud exercitation ullamco laboris nisi ut aliquip ex ea commodo consequat. Duis aute irure dolor in reprehenderit in voluptate velit esse</aside>

  <h3 class="call-h" style="top:99.5px">Lorem ipsum dolor sit amet, cons :</h3>
  <p class="call-t" style="top:110px">"Lorem ipsum dolor sit amet, consectetur adipiscing elit, sed do eiusmod tempor incididunt ut labore et dolore magna aliqua. Ut enim ad minim veniam, quis nostrud exercitation ullamco laboris nisi ut aliquip ex ea commodo consequat. Duis aute irure dolor in</p>
  <aside class="callout" style="top:134px">"Lorem ipsum dolor sit amet, consectetur adipiscing elit, sed do eiusmod tempor incididunt ut labore et dolore magna aliqua. Ut enim ad minim veniam, quis nostrud exercitation ullamco laboris nisi ut aliquip ex ea commodo consequat. Duis aute irure dolor in reprehenderit in voluptate velit esse</aside>

  <h3 class="call-h" style="top:174px">Lorem ipsum dolor sit amet, cons :</h3>
  <p class="call-t" style="top:184.5px">"Lorem ipsum dolor sit amet, consectetur adipiscing elit, sed do eiusmod tempor incididunt ut labore et dolore magna aliqua. Ut enim ad minim veniam, quis nostrud exercitation ullamco laboris nisi ut aliquip ex ea commodo consequat. Duis aute irure dolor in</p>

  <div class="foot-line"></div>
  <div class="foot"><span>"Confidential and Proprietary - For Veltrix Global Internal Use Only,"</span><span class="date">26/03/24</span><span class="pg">X of Y</span></div>
</section>

<!-- Status report table page -->
<section class="page" style="left:805.4px;top:298.6px">
  <p class="conf" style="top:14.5px;left:14px">"Confidential and Proprietary - For Veltrix Global Internal Use Only,"</p>
  <h2 class="doc-title" style="top:20.5px;left:13px">DOCUMENT TITLE</h2>
  <p class="brand-name head-brand" style="top:15px">Veltrix Global</p>

  <div class="report-table">
    <div class="r bar">Lorem ipsum dolor sit</div>
    <div class="r red" style="padding-left:1px">Lorem ipsum dolor sit amet.</div>
    <div class="r"><span class="c1 red">Lorem ipsum</span><span class="c2">Lorem ipsum dolor sit amet.</span><span class="c3 red">Lorem ipsum</span><span>Lorem ipsum dolor sit</span></div>
    <div class="r"><span class="c1 red">Department</span><span class="c2">Enter department</span><span class="c3 red">Manager</span><span>Lorem ipsum dolor sit</span></div>
    <div class="r"><span class="c1 red">Report start date</span><span class="c2">Enter start date</span><span class="c3 red">Report end date</span><span>Lorem ipsum dolor sit</span></div>
    <div class="gap"></div>
    <div class="r bar">Lorem ipsum dolor sit</div>
    <div class="r red"><span class="ca">Action item</span><span class="cb">Due date</span><span>Status</span></div>
    <div class="r"><span class="ca">Enter action item 1</span><span class="cb">Enter due date</span><span>Enter status</span></div>
    <div class="r"><span class="ca">Enter action item 2</span><span class="cb">Enter due date</span><span>Enter status</span></div>
    <div class="r"><span class="ca">Enter action item 3</span><span class="cb">Enter due date</span><span>Enter status</span></div>
    <div class="r"><span class="ca">Enter action item 4</span><span class="cb">Enter due date</span><span>Enter status</span></div>
    <div class="r"><span class="ca">Enter action item 5</span><span class="cb">Enter due date</span><span>Enter status</span></div>
    <div class="r"><span class="ca">Enter action item 6</span><span class="cb">Enter due date</span><span>Enter status</span></div>
    <div class="gap"></div>
    <div class="r bar">Lorem ipsum dolor sit</div>
    <div class="r red"><span class="ca">Goals</span><span class="cb">Due date</span><span>Progress</span></div>
    <div class="r"><span class="ca">Enter goal 1</span><span class="cb">Enter due date</span><span>Enter progress</span></div>
    <div class="r"><span class="ca">Enter goal 2</span><span class="cb">Enter due date</span><span>Enter progress</span></div>
    <div class="r"><span class="ca">Enter goal 3</span><span class="cb">Enter due date</span><span>Enter progress</span></div>
    <div class="r"><span class="ca">Enter goal 4</span><span class="cb">Enter due date</span><span>Enter progress</span></div>
    <div class="r"><span class="ca">Enter goal 5</span><span class="cb">Enter due date</span><span>Enter progress</span></div>
    <div class="r"><span class="ca">Enter goal 6</span><span class="cb">Enter due date</span><span>Enter progress</span></div>
    <div class="gap"></div>
    <div class="r bar">Lorem ipsum dolor sit</div>
    <div class="r" style="padding-left:1px">Enter accomplishments</div>
    <div class="r bar">Lorem ipsum dolor sit</div>
    <div class="r" style="padding-left:1px">Enter concerns</div>
  </div>

  <div class="foot-line"></div>
  <div class="foot"><span>"Confidential and Proprietary - For Veltrix Global Internal Use Only,"</span><span class="date">26/03/24</span><span class="pg">X of Y</span></div>
</section>

<!-- Data sheet table page -->
<section class="page" style="left:1003.8px;top:300px">
  <p class="conf" style="top:15px;left:10px">"Confidential and Proprietary - For Veltrix Global Internal Use Only,"</p>
  <h2 class="doc-title" style="top:20.5px;left:9px">DOCUMENT TITLE</h2>
  <p class="brand-name head-brand" style="top:15px">Veltrix Global</p>

  <p class="sheet-label">Lorem ipsum dolor</p>
  <table class="grid info-grid" style="top:46px">
    <tr><td style="width:23px">Sheet No.</td><td style="width:70px">Enter sheet number</td><td style="width:21px">Date</td><td>Enter date</td></tr>
    <tr><td>Performed By</td><td>Your name</td><td>Department</td><td>Enter department</td></tr>
  </table>

  <table class="grid" style="top:63px">
    <tr><td style="width:26px">Lorem</td><td style="width:44px">Lorem Lorem</td><td style="width:23px">Lorem</td><td style="width:21px">Lorem</td><td>Lorem Lorem</td></tr>
    <tr><td>Enter number 1</td><td>Lorem Lorem</td><td class="rt">Lorem</td><td>Lorem</td><td>Lorem Lorem</td></tr>
    <tr><td>Enter number 2</td><td>Lorem Lorem</td><td class="rt">Lorem</td><td>Lorem</td><td>Lorem Lorem</td></tr>
    <tr><td>Enter number 3</td><td>Lorem Lorem</td><td class="rt">Lorem</td><td>Lorem</td><td>Lorem Lorem</td></tr>
    <tr><td>Enter number 4</td><td>Lorem Lorem</td><td class="rt">Lorem</td><td>Lorem</td><td>Lorem Lorem</td></tr>
    <tr><td>Enter number 5</td><td>Lorem Lorem</td><td class="rt">Lorem</td><td>Lorem</td><td>Lorem Lorem</td></tr>
    <tr><td>Enter number 6</td><td>Lorem Lorem</td><td class="rt">Lorem</td><td>Lorem</td><td>Lorem Lorem</td></tr>
    <tr><td>Enter number 7</td><td>Lorem Lorem</td><td class="rt">Lorem</td><td>Lorem</td><td>Lorem Lorem</td></tr>
    <tr><td>Enter number 8</td><td>Lorem Lorem</td><td class="rt">Lorem</td><td>Lorem</td><td>Lorem Lorem</td></tr>
    <tr><td>Enter number 9</td><td>Lorem Lorem</td><td class="rt">Lorem</td><td>Lorem</td><td>Lorem Lorem</td></tr>
    <tr><td>Enter number 10</td><td>Lorem Lorem</td><td class="rt">Lorem</td><td>Lorem</td><td>Lorem Lorem</td></tr>
    <tr><td>Enter number 11</td><td>Lorem Lorem</td><td class="rt">Lorem</td><td>Lorem</td><td>Lorem Lorem</td></tr>
    <tr><td>Enter number 12</td><td>Lorem Lorem</td><td class="rt">Lorem</td><td>Lorem</td><td>Lorem Lorem</td></tr>
    <tr><td>Enter number 13</td><td>Lorem Lorem</td><td class="rt">Lorem</td><td>Lorem</td><td>Lorem Lorem</td></tr>
    <tr><td>Enter number 14</td><td>Lorem Lorem</td><td class="rt">Lorem</td><td>Lorem</td><td>Lorem Lorem</td></tr>
    <tr><td>Enter number 15</td><td>Lorem Lorem</td><td class="rt">Lorem</td><td>Lorem</td><td>Lorem Lorem</td></tr>
    <tr><td>Enter number 16</td><td>Lorem Lorem</td><td class="rt">Lorem</td><td>Lorem</td><td>Lorem Lorem</td></tr>
    <tr><td>Enter number 17</td><td>Lorem Lorem</td><td class="rt">Lorem</td><td>Lorem</td><td>Lorem Lorem</td></tr>
    <tr><td>Enter number 18</td><td>Lorem Lorem</td><td class="rt">Lorem</td><td>Lorem</td><td>Lorem Lorem</td></tr>
    <tr><td>Enter number 19</td><td>Lorem Lorem</td><td class="rt">Lorem</td><td>Lorem</td><td>Lorem Lorem</td></tr>
    <tr><td>Enter number 20</td><td>Lorem Lorem</td><td class="rt">Lorem</td><td>Lorem</td><td>Lorem Lorem</td></tr>
  </table>

  <div class="sign">Signature<br>~Your signature</div>

  <div class="foot-line"></div>
  <div class="foot"><span>"Confidential and Proprietary - For Veltrix Global Internal Use Only,"</span><span class="date">26/03/24</span><span class="pg">X of Y</span></div>
</section>

</body>
</html>
```